Hi,

I have just started up a business called VELUMO in Melbourne. We run fun street art tours around Melbourne's CBD.

I need to create a design for the back side of my business cards. I have designed the front side (simply with my logo) however, I am having trouble designing the reverse side in a professional manner. I have attached pictures of what I have done.

The picture attached titled "VELUMO Business Cards Back" has all the information that I require on the back side of my business cards; although displayed in an amateur and simple way. As displayed in the picture, I need: the VELUMO logo, the website URL, the booking details (phone - 0481 556 217 & email - bookings@velumo.com.au) and the service description ($20, One Hour, Tours Daily, Meet at Carrow Rd Terminal). I would also like to use the font in the picture supplied which is "source-sans-pro".

The VELUMO tours are for tourists and are relaxed, entertaining and fun! I would like the design to reflect this.

Target Market(s)

Backpackers & University Students

Industry/Entity Type

Business

Requirements
Must have
• The VELUMO logo, the website URL, the booking details (phone - 0481 556 217 & email - bookings@velumo.com.au) and the service description ($20, One Hour, Tours Daily, Meet at Carrow Rd Terminal).

```html
<!DOCTYPE html>
<html lang="en">
<head>
<meta charset="utf-8">
<title>VELUMO Business Cards</title>
<link rel="stylesheet" href="https://fonts.googleapis.com/css2?family=Source+Sans+3:wght@400;600;700;900&display=swap">
<style>
  :root {
    --backdrop: #1f1f21;
    --card-white: #f6f6f6;
    --card-grey: #e4e4e4;
    --brand-red: #d9221c;
    --ink: #1b1b1b;
    --ink-soft: #444444;
    --art-dark: #3a3a3c;
    --art-mid: #8a8b8e;
    --art-light: #d6d6d8;
    --pill: #ececec;
  }
  * { box-sizing: border-box; margin: 0; padding: 0; }
  html, body {
    width: 1200px; height: 750px; overflow: hidden;
    background: var(--backdrop);
    font-family: "Source Sans 3", "Source Sans Pro", Arial, sans-serif;
    color: var(--ink);
  }
  .canvas { position: relative; width: 1200px; height: 750px; }

  .card {
    position: absolute; width: 500px; height: 290px; overflow: hidden;
    background: radial-gradient(ellipse at 40% 45%, var(--card-white) 0%, var(--card-grey) 100%);
    border-top: 5px solid var(--brand-red);
    box-shadow: 0 10px 30px rgba(0,0,0,.45);
  }
  .card--front { left: 70px; top: 110px; border-bottom: 5px solid var(--brand-red); }
  .card--back  { left: 630px; top: 350px; }

  .brand-name {
    font-weight: 900; color: var(--brand-red);
    letter-spacing: 3px; line-height: 1;
  }

  /* Front */
  .front__brand { position: absolute; left: 20px; top: 52px; width: 270px; text-align: center; font-size: 56px; }
  .front__tagline {
    position: absolute; left: 20px; top: 150px; width: 270px; text-align: center;
    font-size: 27px; font-weight: 700; line-height: 1.12; color: var(--ink);
  }
  .front__art {
    position: absolute; right: 0; top: 0; width: 200px; height: 100%;
    background: radial-gradient(ellipse at 45% 40%, var(--art-dark) 0%, var(--art-mid) 45%, var(--art-light) 75%, transparent 100%);
  }

  /* Back */
  .back__art {
    position: absolute; left: 0; top: 0; width: 190px; height: 245px;
    background: radial-gradient(ellipse at 40% 45%, var(--art-dark) 0%, var(--art-mid) 45%, var(--art-light) 75%, transparent 100%);
  }
  .back__brand { position: absolute; left: 200px; right: 20px; top: 28px; text-align: center; font-size: 46px; }

  .tour-facts {
    position: absolute; left: 176px; right: 6px; top: 100px;
    display: flex; align-items: center; justify-content: center; gap: 6px;
    font-weight: 700; font-size: 17px; line-height: 1.05; text-align: center; color: var(--ink);
  }
  .tour-facts__arrow { width: 26px; height: 12px; flex: none; }

  .book-now {
    position: absolute; left: 250px; top: 172px; width: 160px; height: 24px;
    border-radius: 5px; background: linear-gradient(var(--card-white), var(--pill));
    box-shadow: 0 2px 4px rgba(0,0,0,.25);
    font-size: 13px; font-weight: 700; color: var(--ink-soft);
    display: flex; align-items: center; justify-content: center; gap: 4px;
  }
  .book-now__cta { color: var(--brand-red); }

  .contact-row {
    position: absolute; left: 178px; right: 8px; top: 209px;
    display: flex; justify-content: center; gap: 14px;
    font-size: 14px; font-weight: 600; color: var(--ink);
  }
  .contact-item { display: flex; align-items: center; gap: 5px; }
  .contact-item svg { width: 16px; height: 16px; }

  .web-band {
    position: absolute; left: 0; right: 0; bottom: 0; height: 40px;
    background: var(--brand-red); color: #ffffff;
    display: flex; align-items: center; justify-content: center;
    font-size: 18px; font-weight: 700; letter-spacing: .3px;
  }
</style>
</head>
<body>
<main class="canvas">

  <section class="card card--front" aria-label="Business card front">
    <div class="front__brand brand-name">VELUMO</div>
    <p class="front__tagline">Melbourne Street Art<br>Walking Tours</p>
    <div class="front__art" role="img" aria-label="Illustration of a hooded street artist leaping above a city skyline splash"></div>
  </section>

  <section class="card card--back" aria-label="Business card back">
    <div class="back__art" role="img" aria-label="Illustration of a hooded street artist leaping above a city skyline splash"></div>
    <div class="back__brand brand-name">VELUMO</div>

    <div class="tour-facts">
      <span>$20</span>
      <svg class="tour-facts__arrow" viewBox="0 0 26 12"><path d="M0 4h17V0l9 6-9 6V8H0z" fill="var(--brand-red)"/></svg>
      <span>Tours<br>Daily</span>
      <svg class="tour-facts__arrow" viewBox="0 0 26 12"><path d="M0 4h17V0l9 6-9 6V8H0z" fill="var(--brand-red)"/></svg>
      <span>One<br>Hour</span>
      <svg class="tour-facts__arrow" viewBox="0 0 26 12"><path d="M0 4h17V0l9 6-9 6V8H0z" fill="var(--brand-red)"/></svg>
      <span>Meet at<br>Carrow Rd<br>Terminal</span>
    </div>

    <div class="book-now">Call Theo to <span class="book-now__cta">BOOK NOW</span></div>

    <div class="contact-row">
      <span class="contact-item">
        <svg viewBox="0 0 16 16"><circle cx="8" cy="8" r="7" fill="none" stroke="var(--brand-red)" stroke-width="1.4"/><path d="M5.4 4.2l1.4 1.6-.8 1c.5 1.1 1.3 1.9 2.3 2.4l1-.8 1.6 1.4-.9 1.2C7.7 11 4.9 8.3 4.2 5.1z" fill="var(--brand-red)"/></svg>
        0481 556 217
      </span>
      <span class="contact-item">
        <svg viewBox="0 0 16 16"><circle cx="8" cy="8" r="7" fill="none" stroke="var(--brand-red)" stroke-width="1.4"/><rect x="4" y="5.2" width="8" height="5.6" fill="none" stroke="var(--brand-red)" stroke-width="1.1"/><path d="M4 5.4l4 3 4-3" fill="none" stroke="var(--brand-red)" stroke-width="1.1"/></svg>
        bookings@velumo.com.au
      </span>
    </div>

    <div class="web-band">www.velumo.com.au</div>
  </section>

</main>
</body>
</html>
```